Business Card Creation

I am looking for a business card with a double take look... I upload a logo I would like used for its creation. We are an environmental firm that handles indoor air quality, water damages, fire damages, mold, HVAC contaminants, inspections and testing.

I just want to say that all the submissions are exactly what we were looking for and that everything from the font, layout and colors are amazing... Keep up the good work.

```html
<!DOCTYPE html>
<html lang="en">
<head>
<meta charset="utf-8">
<title>R &amp; T Consulting, Inc. — Business Card</title>
<link rel="stylesheet" href="https://fonts.googleapis.com/css2?family=Arimo:wght@400;700&display=swap">
<style>
  :root {
    --stage: #0f2a44;
    --card-dark: #3b3b3b;
    --card-light: #ffffff;
    --card-light-edge: #dcdcdc;
    --brand-blue: #2b96d6;
    --brand-blue-deep: #1e7fc2;
    --brand-orange: #f05a1e;
    --brand-amber: #f7a823;
    --brand-green: #2aa95a;
    --text-light: #e9e9e9;
    --text-grey: #555555;
    --text-dark: #2a2a2a;
    --white: #ffffff;
  }
  * { box-sizing: border-box; margin: 0; padding: 0; }
  html, body { width: 1200px; height: 906px; overflow: hidden; }
  body {
    background: var(--stage);
    font-family: "Arimo", Arial, sans-serif;
    display: flex;
    flex-direction: column;
    align-items: center;
    justify-content: center;
    gap: 34px;
  }
  .card {
    position: relative;
    width: 700px;
    height: 400px;
    border-radius: 26px;
    overflow: hidden;
  }
  /* Back side */
  .card--back {
    background: var(--card-dark);
    display: flex;
    flex-direction: column;
    align-items: center;
    justify-content: center;
    gap: 28px;
  }
  .brand-dot {
    width: 120px;
    height: 120px;
    border-radius: 50%;
    border: 12px solid var(--brand-green);
  }
  .brand-name {
    font-weight: 400;
    letter-spacing: 1px;
    text-transform: uppercase;
  }
  .card--back .brand-name { color: var(--text-light); font-size: 30px; }

  /* Front side */
  .card--front {
    background: radial-gradient(ellipse at 55% 45%, var(--card-light) 40%, var(--card-light-edge) 100%);
  }
  .front-swoosh { position: absolute; inset: 0; }
  .front-brand {
    position: absolute;
    left: 48px;
    top: 150px;
    display: flex;
    align-items: center;
    gap: 14px;
  }
  .front-brand .brand-dot { width: 64px; height: 64px; border-width: 7px; }
  .front-brand .brand-name { color: var(--text-grey); font-size: 18px; }
  .holder {
    position: absolute;
    left: 48px;
    top: 270px;
  }
  .holder-name {
    color: var(--brand-blue);
    font-size: 26px;
    letter-spacing: 1.5px;
    text-transform: uppercase;
  }
  .holder-role {
    color: var(--text-dark);
    font-size: 16px;
    margin-top: 4px;
  }
  .contact {
    position: absolute;
    right: 34px;
    top: 58px;
    text-align: right;
    color: var(--white);
    font-size: 14px;
    line-height: 1.25;
  }
  .contact-address { font-size: 16px; margin-bottom: 22px; line-height: 1.3; }
  .contact-row {
    display: flex;
    justify-content: flex-end;
    align-items: center;
    gap: 8px;
    margin-bottom: 9px;
  }
  .contact-row svg { width: 14px; height: 14px; flex: none; }
  .contact-gap { height: 14px; }
</style>
</head>
<body>

  <section class="card card--back" aria-label="Card back">
    <div class="brand-dot" aria-hidden="true"></div>
    <div class="brand-name">R &amp; T Consulting, Inc.</div>
  </section>

  <section class="card card--front" aria-label="Card front">
    <svg class="front-swoosh" viewBox="0 0 700 400" preserveAspectRatio="none" aria-hidden="true">
      <defs>
        <linearGradient id="blueFill" x1="0" y1="0" x2="1" y2="1">
          <stop offset="0" stop-color="var(--brand-blue)"/>
          <stop offset="1" stop-color="var(--brand-blue-deep)"/>
        </linearGradient>
        <linearGradient id="orangeBand" x1="0" y1="0" x2="0" y2="1">
          <stop offset="0" stop-color="var(--brand-orange)"/>
          <stop offset="1" stop-color="var(--brand-amber)"/>
        </linearGradient>
      </defs>
      <path d="M398 0 C470 120 300 250 350 400 L380 400 C330 250 500 120 430 0 Z" fill="url(#orangeBand)"/>
      <path d="M440 0 C520 120 340 260 400 400 L700 400 L700 0 Z" fill="url(#blueFill)"/>
      <path d="M432 0 C510 120 330 260 390 400" fill="none" stroke="var(--white)" stroke-width="3"/>
      <path d="M462 0 C540 120 362 260 420 400" fill="none" stroke="var(--white)" stroke-width="1.5" opacity="0.8"/>
    </svg>

    <div class="front-brand">
      <div class="brand-dot" aria-hidden="true"></div>
      <div class="brand-name">R &amp; T Consulting, Inc.</div>
    </div>

    <div class="holder">
      <div class="holder-name">Daniel Morrow</div>
      <div class="holder-role">Managing Director</div>
    </div>

    <div class="contact">
      <div class="contact-address">214, 6th floor,<br>Harbor Point Avenue</div>
      <div class="contact-row">555 210 4836
        <svg viewBox="0 0 16 16" aria-hidden="true"><path d="M4 1l3 3-2 2c1 2 3 4 5 5l2-2 3 3-2 3C7 15 1 9 1 3z" fill="var(--white)"/></svg>
      </div>
      <div class="contact-row">555 210 4837
        <svg viewBox="0 0 16 16" aria-hidden="true"><rect x="4" y="1" width="8" height="14" rx="1.5" fill="none" stroke="var(--white)" stroke-width="1.5"/><circle cx="8" cy="12.5" r="0.9" fill="var(--white)"/></svg>
      </div>
      <div class="contact-row">555 210 4838
        <svg viewBox="0 0 16 16" aria-hidden="true"><rect x="2" y="6" width="12" height="8" fill="var(--white)"/><rect x="4" y="2" width="8" height="4" fill="none" stroke="var(--white)" stroke-width="1.4"/></svg>
      </div>
      <div class="contact-gap"></div>
      <div class="contact-row">hello@rtconsult.com
        <svg viewBox="0 0 16 16" aria-hidden="true"><rect x="1" y="3" width="14" height="10" fill="var(--white)"/><path d="M1 3l7 6 7-6" fill="none" stroke="var(--brand-blue)" stroke-width="1.3"/></svg>
      </div>
      <div class="contact-row">www.rtconsultinc.com
        <svg viewBox="0 0 16 16" aria-hidden="true"><circle cx="8" cy="8" r="6.5" fill="none" stroke="var(--white)" stroke-width="1.4"/><ellipse cx="8" cy="8" rx="3" ry="6.5" fill="none" stroke="var(--white)" stroke-width="1.1"/><path d="M1.5 8h13" stroke="var(--white)" stroke-width="1.1"/></svg>
      </div>
    </div>
  </section>

</body>
</html>
```